Law Firm Business Card

This is a business card for a law firm that serves US military and veterans.

The card must have ONLY the following (we want an uncluttered look):

- Company logo (PNG, GIF, JPEG copies uploaded)
- A tagline reading: "a law firm for service members and veterans"
- My name and title: "Martin Okello" and "Attorney"
- My email: "martin.okello@harborlinecounsel.com"
- My number: "855-FILE-NOW (345-3669)"

We are looking for a clean, simple layout with only the above information, likely printed on a bright white cotton stock. The font of our logo is DIN 1451, and the font used on our website is Helvetica Neue. The color of our logo is #336699, and we probably want the tagline in that color also, and my contact information in a dark grey. Please review our website at www.harborlinecounsel.com to ensure your card design complements our website style.

Thanks and we look forward to seeing your submissions.

A few notes:

- Two-sided submissions are ok
- Please don't add graphics (scales of justice, judges hammer, etc)

```html
<!DOCTYPE html>
<html lang="en">
<head>
<meta charset="utf-8">
<title>Harborline Counsel – Business Card</title>
<link href="https://fonts.googleapis.com/css2?family=Lato:wght@400;700;900&display=swap" rel="stylesheet">
<style>
  :root {
    --brand-blue: #336699;
    --accent-blue: #3e72ae;
    --ink-black: #0b0b0c;
    --card-white: #ffffff;
    --backdrop: #3d3d3f;
    --text-light: #ffffff;
  }
  * { margin: 0; padding: 0; box-sizing: border-box; }
  html, body {
    width: 1200px;
    height: 900px;
    overflow: hidden;
    background: var(--backdrop);
    font-family: "Lato", Arial, sans-serif;
  }
  .canvas {
    position: relative;
    width: 1200px;
    height: 900px;
  }
  .business-card {
    position: absolute;
    left: 75px;
    top: 150px;
    width: 1050px;
    height: 600px;
    border-radius: 34px;
    overflow: hidden;
    background: var(--card-white);
  }
  .card-shapes {
    position: absolute;
    inset: 0;
    width: 100%;
    height: 100%;
  }
  .wordmark {
    position: absolute;
    top: 108px;
    left: 0;
    width: 100%;
    text-align: center;
    color: var(--brand-blue);
    font-weight: 900;
    font-size: 62px;
    letter-spacing: 2px;
    text-transform: uppercase;
    line-height: 1;
  }
  .name-block {
    position: absolute;
    left: 52px;
    top: 412px;
    color: var(--text-light);
  }
  .name {
    font-size: 44px;
    font-weight: 400;
    line-height: 1.05;
  }
  .name strong { font-weight: 700; }
  .title {
    display: block;
    text-align: right;
    font-size: 22px;
    font-weight: 400;
    margin-top: 2px;
  }
  .contact {
    position: absolute;
    right: 42px;
    top: 362px;
    color: var(--text-light);
    font-size: 22px;
    line-height: 1.75;
    text-align: left;
  }
  .contact dt {
    display: inline;
    font-weight: 700;
  }
  .contact dd {
    display: inline;
    font-weight: 400;
  }
  .contact .row { display: block; }
  .contact .row.phone { padding-left: 92px; }
  .tagline {
    position: absolute;
    left: 0;
    bottom: 28px;
    width: 100%;
    text-align: center;
    color: var(--accent-blue);
    font-size: 25px;
    font-weight: 700;
    letter-spacing: 4.6px;
    text-transform: uppercase;
  }
</style>
</head>
<body>
<main class="canvas">
  <section class="business-card" aria-label="Harborline Counsel business card">
    <svg class="card-shapes" viewBox="0 0 1050 600" preserveAspectRatio="none" aria-hidden="true">
      <!-- top-right corner tab -->
      <path d="M860 0 H1050 V50 H915 C890 50 880 20 860 0 Z" fill="var(--accent-blue)"/>
      <!-- lower dark band with sweeping curve -->
      <path d="M0 420 H470 C540 420 560 300 640 270 C680 256 720 258 760 258 H1050 V600 H0 Z" fill="var(--ink-black)"/>
      <!-- name tab -->
      <path d="M0 395 H420 C470 395 480 430 500 470 C510 492 500 510 470 510 H0 Z" fill="var(--accent-blue)"/>
    </svg>

    <h1 class="wordmark">Harborline Counsel</h1>

    <div class="name-block">
      <p class="name">Martin <strong>Okello</strong></p>
      <span class="title">Attorney</span>
    </div>

    <dl class="contact">
      <div class="row phone"><dt>number:</dt> <dd>855-FILE-NOW (345-3669)</dd></div>
      <div class="row email"><dt>email:</dt> <dd>martin.okello@harborlinecounsel.com</dd></div>
    </dl>

    <p class="tagline">A law firm for service members and veterans</p>
  </section>
</main>
</body>
</html>
```